Shine Barn Auto Care Business Card

2 side business card design for an auto detailing business

Target Market(s)

Auto detailing

Contact Information for Business Card

Things included

The business name “Shine Barn Auto Care”
Owen Marchetti
(403)871-2964
Willowbend, Sk

Services offered - complete interior& exterior detail
- paint correction & protection
- ceramic coating
- trim restore
- auto carpet & seat cleaning

Requirements
Must have
• Colours that are in my logo

Services offered

My name Owen Marchetti
403-871-2964
Willowbend, Sk

Not too sure in what order for these ?
Website. Shinebarnautocare.com
Instagram Shinebarnautocare
Email. Shinebarnautoac@mailbox-example.com

```html
<!DOCTYPE html>
<html lang="en">
<head>
<meta charset="utf-8">
<title>Shine Barn Auto Care – Business Card</title>
<link rel="stylesheet" href="https://fonts.googleapis.com/css2?family=Figtree:wght@400;500;700;800&display=swap">
<style>
  :root {
    --backdrop: #e4e4e4;
    --card-light: #f4f4f6;
    --card-dark: #241e25;
    --maroon: #8a0f12;
    --ink: #1b1b1b;
    --text-light: #f2f2f2;
    --emboss: #2e2730;
    --emboss-edge: #191419;
  }
  * { box-sizing: border-box; margin: 0; padding: 0; }
  html, body { width: 1200px; height: 1200px; overflow: hidden; }
  body {
    background: var(--backdrop);
    font-family: "Figtree", sans-serif;
    position: relative;
  }
  .card {
    position: absolute;
    left: 209px;
    width: 797px;
    height: 442px;
    overflow: hidden;
  }
  .card--front { top: 98px; background: var(--card-light); }
  .card--back { top: 634px; background: var(--card-dark); }

  /* front */
  .brand {
    position: absolute;
    left: 0;
    top: 136px;
    width: 420px;
    text-align: center;
  }
  .brand__dot {
    display: block;
    width: 100px;
    height: 100px;
    margin: 0 auto 16px;
    border: 10px solid var(--maroon);
    border-radius: 50%;
  }
  .brand__name {
    font-weight: 800;
    font-size: 34px;
    letter-spacing: 1px;
    line-height: 1.05;
    color: var(--ink);
    text-transform: uppercase;
  }
  .divider {
    position: absolute;
    left: 397px;
    top: 127px;
    width: 2px;
    height: 188px;
    background: var(--ink);
  }
  .person {
    position: absolute;
    left: 442px;
    top: 118px;
  }
  .person__name {
    font-weight: 800;
    font-size: 30px;
    color: var(--maroon);
    line-height: 1.1;
  }
  .person__role {
    font-size: 19px;
    color: var(--ink);
    margin-top: 3px;
  }
  .contact {
    list-style: none;
    margin-top: 20px;
  }
  .contact__item {
    display: flex;
    align-items: center;
    gap: 6px;
    font-size: 19px;
    font-weight: 500;
    color: var(--ink);
    height: 25.5px;
    white-space: nowrap;
  }
  .contact__item--email { font-size: 15px; }
  .contact__icon { width: 15px; height: 15px; flex: none; }

  /* back */
  .back-name {
    position: absolute;
    left: 53px;
    top: 190px;
    font-weight: 800;
    font-size: 34px;
    letter-spacing: 1px;
    line-height: 1.05;
    color: var(--text-light);
    text-transform: uppercase;
  }
  .back-ring {
    position: absolute;
    left: 394px;
    top: 41px;
    width: 360px;
    height: 360px;
    border-radius: 50%;
    border: 26px solid var(--emboss);
    box-shadow: inset 1px 2px 2px var(--emboss-edge), 1px 2px 2px var(--emboss-edge);
  }
</style>
</head>
<body>

<section class="card card--front">
  <div class="brand">
    <span class="brand__dot"></span>
    <p class="brand__name">Shine Barn<br>Auto Care</p>
  </div>

  <div class="divider"></div>

  <div class="person">
    <h1 class="person__name">Owen Marchetti</h1>
    <p class="person__role">Co-president</p>
    <ul class="contact">
      <li class="contact__item">
        <svg class="contact__icon" viewBox="0 0 16 16"><path fill="#8a0f12" d="M8 0a5.5 5.5 0 0 0-5.5 5.5C2.5 9.6 8 16 8 16s5.5-6.4 5.5-10.5A5.5 5.5 0 0 0 8 0zm0 8a2.5 2.5 0 1 1 0-5 2.5 2.5 0 0 1 0 5z"/></svg>
        Willowbend, Sk
      </li>
      <li class="contact__item">
        <svg class="contact__icon" viewBox="0 0 16 16"><path fill="#8a0f12" d="M3.6 1l2.2 3-1.3 1.6a9 9 0 0 0 5 5L11 9.3l3 2.2-1.2 2.9C7 14.5 1.5 9 1.6 3.2z"/><path d="M9 1.5a5.5 5.5 0 0 1 5.5 5.5M9 4a3 3 0 0 1 3 3" stroke="#8a0f12" stroke-width="1.3" fill="none"/></svg>
        403-871-2964
      </li>
      <li class="contact__item contact__item--email">
        <svg class="contact__icon" viewBox="0 0 16 16"><rect x="0.5" y="3" width="15" height="10.5" rx="1" fill="#8a0f12"/><path d="M1 3.8l7 5 7-5" stroke="#f4f4f6" stroke-width="1.2" fill="none"/></svg>
        Shinebarnautocare@mailbox-example.com
      </li>
      <li class="contact__item">
        <svg class="contact__icon" viewBox="0 0 16 16"><rect x="1.5" y="1.5" width="13" height="13" rx="3" fill="none" stroke="#8a0f12" stroke-width="1.6"/></svg>
        Shinebarnautocare
      </li>
      <li class="contact__item">
        <svg class="contact__icon" viewBox="0 0 16 16"><circle cx="8" cy="8" r="6.8" fill="none" stroke="#8a0f12" stroke-width="1.5"/><path d="M1.5 8h13M8 1.2c-3 3.5-3 10.1 0 13.6M8 1.2c3 3.5 3 10.1 0 13.6" stroke="#8a0f12" stroke-width="1.1" fill="none"/></svg>
        www.Shinebarnautocare.com
      </li>
    </ul>
  </div>
</section>

<section class="card card--back">
  <p class="back-name">Shine Barn<br>Auto Care</p>
  <div class="back-ring"></div>
</section>

</body>
</html>
```